MBRT Needs Fundraiser Dinner Invite!!

The Marita Brenkoll Foundation, a 501 3(c) non for profit has a yearly fundraiser, with varying themes. Last year it was "cowboys" and "cowgirls"
This year, it is Parlor 88, or 70's disco music. I have uploaded last years invite for reference, some stock photography for inspiration. You are not limited to using the stock photos.

Annual MBRT Fundraiser Dinner
October 13th, 2022
Starts: 6:30pm
RSVP By: September 20th
Place: The Oxmere
Price: $135 per ticket

Target Market(s)

Donors, Business People, Every person

Industry/Entity Type

Non for Profit

Font styles to use
Sans Serif

Colors
0054AA
0677BA
7BADD7
CADEEF
E8F1F8
E54698
E96AAD
F1A4CE
F9D9EA
FCEFF6
6B429C
8869AF
B7A5CE
E3DAEB
F3F0F8

Requirements
Must have
• The invite should be 5x7, be sophisticated as the clientele are mainly business people that come to support the cause. It should be fun and inviting at the same time.

```html
<!DOCTYPE html>
<html lang="en">
<head>
<meta charset="utf-8">
<title>Annual MBRT Fundraiser Dinner Invitation</title>
<link rel="stylesheet" href="https://fonts.googleapis.com/css2?family=Fredoka:wght@600;700&family=Poppins:wght@600;700&family=Kalam&display=swap">
<style>
  :root {
    --navy: #34334b;
    --navy-light: #3c3b55;
    --yellow: #f9c614;
    --teal: #24a9ac;
    --cream: #fdf8e2;
    --page: #ffffff;
  }
  html, body {
    margin: 0;
    padding: 0;
    width: 1200px;
    height: 1200px;
    overflow: hidden;
    background: var(--page);
  }
  .invite {
    position: absolute;
    left: 188px;
    top: 20px;
    width: 824px;
    height: 1160px;
  }
  .invite svg { display: block; width: 100%; height: 100%; }
  .kicker { font-family: "Fredoka", sans-serif; font-weight: 700; fill: var(--yellow); }
  .headline-top { font-family: "Fredoka", sans-serif; font-weight: 700; fill: var(--teal); }
  .headline-main { font-family: "Poppins", sans-serif; font-weight: 700; fill: var(--cream); }
  .date-line { font-family: "Poppins", sans-serif; font-weight: 600; fill: var(--cream); }
  .venue { font-family: "Fredoka", sans-serif; font-weight: 700; fill: var(--yellow); }
  .rsvp { font-family: "Kalam", cursive; fill: var(--cream); }
  .price { font-family: "Poppins", sans-serif; font-weight: 600; fill: var(--navy); }
</style>
</head>
<body>
<div class="invite">
  <svg viewBox="0 0 860 1210" xmlns="http://www.w3.org/2000/svg">
    <defs>
      <clipPath id="card-clip"><rect width="860" height="1210"/></clipPath>
      <radialGradient id="ball-tone" cx="0.5" cy="0.4" r="0.6">
        <stop offset="0" stop-color="#fdf8e2"/>
        <stop offset="1" stop-color="#cfcab8"/>
      </radialGradient>
    </defs>

    <g clip-path="url(#card-clip)">
      <rect class="card-bg" width="860" height="1210" fill="var(--navy)"/>

      <!-- light rays -->
      <polygon points="300,200 560,200 860,760 860,980 0,980 0,760" fill="var(--navy-light)" opacity="0.6"/>

      <!-- inner frame -->
      <rect x="38" y="40" width="782" height="1132" fill="none" stroke="var(--teal)" stroke-width="2"/>

      <!-- mirror ball area -->
      <circle cx="431" cy="-2" r="249" fill="url(#ball-tone)" role="img" aria-label="Disco mirror ball illustration"/>

      <!-- top-left decorations -->
      <g class="deco-arrows" stroke="var(--yellow)" stroke-width="3">
        <line x1="104" y1="20" x2="104" y2="60"/>
        <line x1="96" y1="25" x2="96" y2="55"/>
        <line x1="88" y1="30" x2="88" y2="50"/>
        <line x1="80" y1="35" x2="80" y2="45"/>
      </g>
      <circle cx="72" cy="165" r="70" fill="none" stroke="var(--cream)" stroke-width="3" stroke-dasharray="14 10"/>
      <polygon points="13,163 85,287 0,287" fill="none" stroke="var(--yellow)" stroke-width="2"/>

      <!-- top-right decorations -->
      <polygon points="818,77 765,170 870,170" fill="none" stroke="var(--cream)" stroke-width="2"/>
      <polygon points="815,0 860,0 860,40 838,40" fill="var(--cream)"/>

      <!-- headline -->
      <text class="kicker" x="430" y="355" font-size="62" text-anchor="middle">Annual MBRT</text>
      <text class="headline-top" x="100" y="483" font-size="118" textLength="682" lengthAdjust="spacingAndGlyphs">FUNDRAISER</text>
      <text class="headline-main" x="92" y="677" font-size="200" textLength="688" lengthAdjust="spacingAndGlyphs">DINNER</text>

      <!-- slashes -->
      <polygon points="423,747 437,747 532,607 518,607" fill="var(--yellow)"/>
      <polygon points="448,747 462,747 557,607 543,607" fill="var(--yellow)"/>
      <polygon points="698,805 724,805 860,582 860,540" fill="var(--yellow)"/>
      <polygon points="764,805 790,805 860,690 860,648" fill="var(--yellow)"/>

      <!-- left triangles -->
      <polygon points="38,670 112,800 0,800 0,735" fill="var(--cream)"/>
      <polygon points="58,820 75,790 92,820" fill="var(--yellow)"/>

      <!-- details -->
      <text class="date-line" x="415" y="830" font-size="42" text-anchor="middle">October 13<tspan font-size="24" dy="-16">th</tspan><tspan dy="16"> at 6.30pm</tspan></text>
      <text class="venue" x="430" y="943" font-size="94" text-anchor="middle" textLength="700" lengthAdjust="spacingAndGlyphs">THE OXMERE</text>
      <text class="rsvp" x="430" y="1022" font-size="44" text-anchor="middle">RSVP By: September 20<tspan font-size="26" dy="-18">th</tspan></text>

      <rect class="price-band" x="202" y="1062" width="455" height="60" fill="var(--teal)"/>
      <text class="price" x="430" y="1108" font-size="44" text-anchor="middle">$135 per ticket</text>

      <!-- bottom corners -->
      <polygon points="35,1005 95,1005 0,1158 0,1062" fill="var(--cream)"/>
      <polygon points="50,1060 72,1060 0,1176 0,1140" fill="var(--yellow)"/>
      <polygon points="780,1210 798,1210 860,1110 860,1080" fill="var(--yellow)"/>
      <polygon points="820,1190 831,1190 860,1142 860,1124" fill="var(--cream)"/>
    </g>
  </svg>
</div>
</body>
</html>
```